Spice Mix Label Bottle Branding - Health and Weight Loss Mixes

The company is called ZestRow Spice Mix's. We've created 5 spice mixes using ingredients that promote health and weight loss. We already have a logo but now we need labels for our bottles. We would like to see designs that have the feel of health supplements (see attached examples)

We would like a different colour featured with each of our flavours.

Our flavours are:
-Golden Chai (Yellow)
-Mild Curry (Orange)
-Coffee Rub (brown)
-Garlic Oregano (Green)
-Taco (Blue)

Thank you!

Target Market(s)

Ages 22-35. Men and Female. Trendy, Hipster.

Industry/Entity Type

Food Production

Font styles to use
Sans Serif

Colors
f37122
0655a3
0692cd
9bcb3c
fbee3f

Requirements
Must have
• A different featured colour for each flavour.
• The ZestRow Spices Logo (attached)
• The slogan: "Weight Loss Ingredients"
• -Golden Chai (Yellow)
• -Mild Curry (Orange)
• -Coffee Rub (brown)
• -Garlic Oregano (Green)
• -Taco (Blue)
• Text Files attached.
Nice to have
• A black label with a featured colour for each of the spice mice flavours.
• 'No Salt added'

```html
<!DOCTYPE html>
<html lang="en">
<head>
<meta charset="utf-8">
<title>ZestRow Spices – Bottle Labels</title>
<link rel="stylesheet" href="https://fonts.googleapis.com/css2?family=Montserrat:wght@300;400;500;600;700;800&display=swap">
<style>
  :root{
    --canvas:#f3f3f4;
    --paper:#ffffff;
    --paper-shade:#ebebed;
    --ink:#2b2b2b;
    --ink-soft:#555555;
    --green:#9cba47;
    --brown:#ae7a45;
    --gold:#c8ad3c;
    --orange:#e9672d;
    --blue:#3e77a8;
  }
  *{box-sizing:border-box;margin:0;padding:0}
  html,body{width:1200px;height:683px;overflow:hidden;background:var(--canvas)}
  body{font-family:"Montserrat",Arial,sans-serif;color:var(--ink)}
  .label-row{
    position:absolute;left:31px;top:181px;
    display:flex;gap:22px;
  }
  .label{
    position:relative;width:210px;height:320px;
    background:var(--paper);overflow:hidden;
    box-shadow:0 2px 10px rgba(0,0,0,.08);
  }
  .label--green{--feature:var(--green)}
  .label--brown{--feature:var(--brown)}
  .label--gold{--feature:var(--gold)}
  .label--orange{--feature:var(--orange)}
  .label--blue{--feature:var(--blue)}
  .label__bg{position:absolute;inset:0;width:100%;height:100%}
  .label__bg .band{fill:var(--feature)}
  .label__bg .shade{fill:var(--paper-shade)}
  .brand{
    position:absolute;top:42px;left:0;right:0;text-align:center;color:var(--paper);
  }
  .brand__name{font-size:23px;font-weight:800;letter-spacing:.5px;line-height:1}
  .brand__tagline{margin-top:8px;font-size:7px;font-weight:700;letter-spacing:.6px;text-transform:uppercase}
  .content{position:absolute;left:18px;right:14px;top:170px}
  .flavour{font-size:19px;font-weight:600;color:var(--feature);line-height:1;text-transform:uppercase}
  .slogan{margin-top:3px;font-size:13px;font-weight:400;text-transform:uppercase;letter-spacing:-.2px}
  .details{margin-top:12px;font-size:6.4px;line-height:1.45;color:var(--ink-soft);width:150px}
  .footer{position:absolute;left:18px;right:12px;bottom:18px;display:flex;justify-content:space-between;align-items:flex-end}
  .footer__type{font-size:9.5px;font-weight:500;color:var(--ink-soft)}
  .dose{position:relative;width:46px;height:40px}
  .dose svg{position:absolute;inset:0}
  .dose polygon{fill:var(--feature)}
  .dose span{position:absolute;left:0;right:0;bottom:7px;text-align:center;font-size:10px;font-weight:600;color:var(--paper)}
</style>
</head>
<body>
<main class="label-row">
  <!-- repeated label -->
  <section class="label label--green">
    <svg class="label__bg" viewBox="0 0 210 320" preserveAspectRatio="none" aria-hidden="true">
      <path class="shade" d="M210 150 L210 320 L120 320 C160 250 190 200 210 150 Z"/>
      <path class="band" d="M0 0 H210 V125 C150 150 70 165 0 145 Z"/>
    </svg>
    <div class="brand"><p class="brand__name">ZestRow Spices</p><p class="brand__tagline">Weight Loss Seasonings</p></div>
    <div class="content">
      <h2 class="flavour">Mild Curry</h2>
      <p class="slogan">Ingredients</p>
      <p class="details">Special Formulated with Garcinia Cambogia, Green Coffee, and Raspberry Ketone to support Metabolism and weight loss*</p>
    </div>
    <div class="footer"><span class="footer__type">Dietary Supplement</span><div class="dose"><svg viewBox="0 0 46 40"><polygon points="23,0 46,10 46,40 0,40 0,10"/></svg><span>200mg</span></div></div>
  </section>

  <section class="label label--brown">
    <svg class="label__bg" viewBox="0 0 210 320" preserveAspectRatio="none" aria-hidden="true">
      <path class="shade" d="M210 150 L210 320 L120 320 C160 250 190 200 210 150 Z"/>
      <path class="band" d="M0 0 H210 V125 C150 150 70 165 0 145 Z"/>
    </svg>
    <div class="brand"><p class="brand__name">ZestRow Spices</p><p class="brand__tagline">Weight Loss Seasonings</p></div>
    <div class="content">
      <h2 class="flavour">Mild Curry</h2>
      <p class="slogan">Ingredients</p>
      <p class="details">Special Formulated with Garcinia Cambogia, Green Coffee, and Raspberry Ketone to support Metabolism and weight loss*</p>
    </div>
    <div class="footer"><span class="footer__type">Dietary Supplement</span><div class="dose"><svg viewBox="0 0 46 40"><polygon points="23,0 46,10 46,40 0,40 0,10"/></svg><span>200mg</span></div></div>
  </section>

  <section class="label label--gold">
    <svg class="label__bg" viewBox="0 0 210 320" preserveAspectRatio="none" aria-hidden="true">
      <path class="shade" d="M210 150 L210 320 L120 320 C160 250 190 200 210 150 Z"/>
      <path class="band" d="M0 0 H210 V125 C150 150 70 165 0 145 Z"/>
    </svg>
    <div class="brand"><p class="brand__name">ZestRow Spices</p><p class="brand__tagline">Weight Loss Seasonings</p></div>
    <div class="content">
      <h2 class="flavour">Mild Curry</h2>
      <p class="slogan">Ingredients</p>
      <p class="details">Special Formulated with Garcinia Cambogia, Green Coffee, and Raspberry Ketone to support Metabolism and weight loss*</p>
    </div>
    <div class="footer"><span class="footer__type">Dietary Supplement</span><div class="dose"><svg viewBox="0 0 46 40"><polygon points="23,0 46,10 46,40 0,40 0,10"/></svg><span>200mg</span></div></div>
  </section>

  <section class="label label--orange">
    <svg class="label__bg" viewBox="0 0 210 320" preserveAspectRatio="none" aria-hidden="true">
      <path class="shade" d="M210 150 L210 320 L120 320 C160 250 190 200 210 150 Z"/>
      <path class="band" d="M0 0 H210 V125 C150 150 70 165 0 145 Z"/>
    </svg>
    <div class="brand"><p class="brand__name">ZestRow Spices</p><p class="brand__tagline">Weight Loss Seasonings</p></div>
    <div class="content">
      <h2 class="flavour">Mild Curry</h2>
      <p class="slogan">Ingredients</p>
      <p class="details">Special Formulated with Garcinia Cambogia, Green Coffee, and Raspberry Ketone to support Metabolism and weight loss*</p>
    </div>
    <div class="footer"><span class="footer__type">Dietary Supplement</span><div class="dose"><svg viewBox="0 0 46 40"><polygon points="23,0 46,10 46,40 0,40 0,10"/></svg><span>200mg</span></div></div>
  </section>

  <section class="label label--blue">
    <svg class="label__bg" viewBox="0 0 210 320" preserveAspectRatio="none" aria-hidden="true">
      <path class="shade" d="M210 150 L210 320 L120 320 C160 250 190 200 210 150 Z"/>
      <path class="band" d="M0 0 H210 V125 C150 150 70 165 0 145 Z"/>
    </svg>
    <div class="brand"><p class="brand__name">ZestRow Spices</p><p class="brand__tagline">Weight Loss Seasonings</p></div>
    <div class="content">
      <h2 class="flavour">Mild Curry</h2>
      <p class="slogan">Ingredients</p>
      <p class="details">Special Formulated with Garcinia Cambogia, Green Coffee, and Raspberry Ketone to support Metabolism and weight loss*</p>
    </div>
    <div class="footer"><span class="footer__type">Dietary Supplement</span><div class="dose"><svg viewBox="0 0 46 40"><polygon points="23,0 46,10 46,40 0,40 0,10"/></svg><span>200mg</span></div></div>
  </section>
</main>
</body>
</html>
```